Medical Eye Care Practice needs a unique business card design.

I need a business card for my medical, eye care practice. I am seeking a unique design, possibly with a vertical or atypical shape layout -- something to make the card stand out. I would like the final design to communicate health and wellness with a contemporary feel. Please incorporate my logo and slogan with a color scheme based off of my logo. It should also identify all of the information that is listed on my sample business card. The back side should be utilized for appointment reminder with date, time, and room for notes. I would also like some incorporation of facebook, twitter, and google plus links.

```html
<!DOCTYPE html>
<html lang="en">
<head>
<meta charset="utf-8">
<title>Brightwater Vision Care – Business Card</title>
<link rel="stylesheet" href="https://fonts.googleapis.com/css2?family=Lato:wght@400;700&display=swap">
<style>
  :root {
    --backdrop: #2a2a2c;
    --paper: #ffffff;
    --brown: #917b58;
    --green: #9db64c;
    --blue: #a8cfea;
    --blue-text: #7fb3d8;
  }
  * { margin: 0; padding: 0; box-sizing: border-box; }
  html, body { width: 1200px; height: 900px; overflow: hidden; }
  body {
    background: var(--backdrop);
    font-family: "Lato", Arial, sans-serif;
    position: relative;
  }
  .card {
    position: absolute;
    top: 150px;
    width: 343px;
    height: 600px;
    background: var(--paper);
    border-radius: 12px;
    overflow: hidden;
    text-align: center;
  }
  .card--front { left: 210px; }
  .card--back { left: 647px; }

  .card__footer {
    position: absolute; left: 0; right: 0; bottom: 0; height: 74px;
    display: flex; flex-direction: column; justify-content: flex-end;
  }
  .card__footer .stripe--blue { height: 6px; background: var(--blue); margin-bottom: 6px; }
  .card__footer .stripe--green { height: 12px; background: var(--green); margin-bottom: 6px; }
  .card__footer .stripe--brown { height: 38px; background: var(--brown); }

  .brand {
    display: flex; align-items: center; justify-content: center; gap: 10px;
    padding-top: 46px;
  }
  .brand__dot { width: 18px; height: 18px; border-radius: 50%; background: var(--green); flex: none; }
  .brand__name { color: var(--brown); font-weight: 700; font-size: 24px; letter-spacing: 0.5px; }

  .slogan { color: var(--blue-text); font-size: 12px; letter-spacing: 1px; text-transform: uppercase; margin-top: 14px; }
  .website-small { color: var(--blue-text); font-size: 12px; margin-top: 3px; }
  .services { color: var(--brown); font-size: 13px; line-height: 1.35; margin: 14px 26px 0; }

  .person { margin-top: 46px; }
  .person__name { color: var(--green); font-size: 26px; font-weight: 400; letter-spacing: 1px; }
  .person__title { color: var(--blue-text); font-size: 14px; margin-top: 2px; }

  .contact { margin-top: 24px; font-size: 15px; line-height: 1.4; color: var(--green); }
  .contact b { color: var(--brown); }

  .card--back .brand { padding-top: 64px; }
  .appointment__title {
    color: var(--green); font-size: 24px; font-weight: 400; letter-spacing: 1.5px; margin-top: 40px;
  }
  .appointment__fields { list-style: none; text-align: left; margin: 22px 0 0 32px; color: var(--brown); font-size: 16px; }
  .appointment__fields li { height: 32px; }
  .appointment__fields .notes { height: 84px; }
  .back__contact { color: var(--green); font-weight: 700; font-size: 16px; line-height: 1.3; }
  .social { display: flex; justify-content: center; gap: 10px; margin-top: 10px; }
  .social span { width: 24px; height: 24px; border-radius: 50%; background: var(--blue); }
</style>
</head>
<body>

<section class="card card--front">
  <header class="brand">
    <span class="brand__dot"></span>
    <span class="brand__name">Brightwater Vision Care</span>
  </header>
  <p class="slogan">Clear Sight • Whole Health • Every Day</p>
  <p class="website-small">www.brightwater-vision.com</p>
  <p class="services">Family Eye Care, Low Vision Rehabilitation, Urgent Care, Ocular Disease, Dry Eye, Retinal Wellness, Ocular Nutrition.</p>

  <div class="person">
    <h1 class="person__name">DANA MERRITT</h1>
    <p class="person__title">OD, FAAO</p>
  </div>

  <div class="contact">
    <p><b>T:</b> (555) 014-2210</p>
    <p><b>F:</b> (555) 014-2211</p>
    <p><b>A:</b> 418 Birch Lane, Suite 210</p>
    <p>Millbrook, WI 53099</p>
  </div>

  <div class="card__footer" aria-hidden="true">
    <div class="stripe--blue"></div>
    <div class="stripe--green"></div>
    <div class="stripe--brown"></div>
  </div>
</section>

<section class="card card--back">
  <header class="brand">
    <span class="brand__dot"></span>
    <span class="brand__name">Brightwater Vision Care</span>
  </header>
  <h2 class="appointment__title">APPOINTMENT</h2>
  <ul class="appointment__fields">
    <li>Date:</li>
    <li>Time:</li>
    <li class="notes">Reason for Visit:</li>
  </ul>
  <div class="back__contact">
    <p>www.brightwater-vision.com</p>
    <p>(555) 014-2210</p>
  </div>
  <div class="social" aria-label="Social links">
    <span></span><span></span><span></span>
  </div>

  <div class="card__footer" aria-hidden="true">
    <div class="stripe--blue"></div>
    <div class="stripe--green"></div>
    <div class="stripe--brown"></div>
  </div>
</section>

</body>
</html>
```